Logo and animation for a set-top box for IPTV

We manufacture a set top box for IPTV. We need a better looking new boot up sequence. The process looks like that:
1. Logo (QV410/QV520/QV630) (needed in bot raster and vector)
2. "Loading" - here we want to have some kind of a better looking picture and and animation that consist of 30 frames- 30 separated image files.
3. "Waiting for network" screen should be changed to be with same design of the previous two screens. We must keep the bottom text too.

All images are 1920х1080

Attaching our current images.

As on the attached pictures.

```html
<!DOCTYPE html>
<html lang="en">
<head>
<meta charset="utf-8">
<title>Loading sequence – first and last frame</title>
<link rel="stylesheet" href="https://fonts.googleapis.com/css2?family=Exo+2:ital,wght@1,700;1,800&display=swap">
<style>
  :root {
    --page: #ffffff;
    --screen: #05090a;
    --ink: #0a0a0a;
    --type: #ffffff;
    --dot-grey: #8a8a8a;
    --spark: rgba(245, 160, 32, 0.95);
    --spark-mid: rgba(200, 135, 50, 0.45);
    --spark-faint: rgba(245, 160, 32, 0.12);
    --clear: rgba(245, 160, 32, 0);
  }
  html, body {
    margin: 0;
    padding: 0;
    overflow: hidden;
    background: var(--page);
  }
  .canvas {
    position: relative;
    width: 1200px;
    height: 1200px;
    overflow: hidden;
    background: var(--page);
    font-family: "Exo 2", sans-serif;
  }
  .frame-label {
    position: absolute;
    margin: 0;
    font-style: italic;
    font-weight: 800;
    font-size: 16.5px;
    letter-spacing: 0.2px;
    color: var(--ink);
    line-height: 1;
  }
  .frame-label--first { left: 53px; top: 65px; }
  .frame-label--last { right: 48px; top: 1126px; }
  .screen-column {
    position: absolute;
    top: 110px;
    width: 526px;
    height: 980px;
    background: var(--screen);
  }
  .screen-column--first { left: 47px; }
  .screen-column--last { left: 627px; }
  .loading-word {
    position: absolute;
    left: 204px;
    margin: 0;
    font-style: italic;
    font-weight: 700;
    font-size: 30px;
    font-variant: small-caps;
    color: var(--type);
    line-height: 1;
    letter-spacing: 0.3px;
  }
  .loading-word--1 { top: 134px; }
  .loading-word--2 { top: 362px; }
  .loading-word--3 { top: 589px; }
  .loading-word--4 { top: 817px; }
  .dots {
    position: absolute;
    left: 0;
    top: 0;
    width: 526px;
    height: 980px;
  }
  .spark-glow {
    position: absolute;
    border-radius: 50%;
    transform: translate(-50%, -50%);
  }
  .spark-glow--single {
    left: 364px; top: 157px; width: 12px; height: 12px;
    background: radial-gradient(circle, var(--spark) 0 30%, var(--clear) 70%);
  }
  .spark-glow--cluster {
    left: 364px; top: 384px; width: 30px; height: 30px;
    background: radial-gradient(circle, var(--spark) 0 12%, var(--spark-mid) 30%, var(--clear) 70%);
  }
  .spark-glow--burst {
    left: 365px; top: 610px; width: 96px; height: 90px;
    background: radial-gradient(circle, var(--spark-faint) 0 35%, var(--spark-mid) 60%, var(--clear) 75%);
  }
  .spark-glow--embers {
    left: 370px; top: 843px; width: 110px; height: 110px;
    background: radial-gradient(circle, var(--clear) 0 40%, var(--spark-faint) 60%, var(--clear) 75%);
  }
</style>
</head>
<body>
<div class="canvas">
  <p class="frame-label frame-label--first">1ST FRAME</p>

  <section class="screen-column screen-column--first" aria-label="Loading animation, opening frames">
    <p class="loading-word loading-word--1">Loading</p>
    <p class="loading-word loading-word--2">Loading</p>
    <p class="loading-word loading-word--3">Loading</p>
    <p class="loading-word loading-word--4">Loading</p>
    <svg class="dots" viewBox="0 0 526 980" aria-hidden="true">
      <circle cx="306" cy="383" r="3.2" fill="var(--dot-grey)"/>
      <circle cx="312" cy="612" r="3" fill="var(--dot-grey)"/>
      <circle cx="328" cy="612" r="3" fill="var(--dot-grey)"/>
      <circle cx="333" cy="840" r="3" fill="var(--dot-grey)"/>
      <circle cx="362" cy="840" r="3.3" fill="var(--type)"/>
    </svg>
  </section>

  <section class="screen-column screen-column--last" aria-label="Loading animation, closing frames">
    <p class="loading-word loading-word--1">Loading</p>
    <div class="spark-glow spark-glow--single" role="img" aria-label="Single orange spark"></div>
    <p class="loading-word loading-word--2">Loading</p>
    <div class="spark-glow spark-glow--cluster" role="img" aria-label="Small cluster of orange sparks"></div>
    <p class="loading-word loading-word--3">Loading</p>
    <div class="spark-glow spark-glow--burst" role="img" aria-label="Burst of orange and grey particles"></div>
    <p class="loading-word loading-word--4">Loading</p>
    <div class="spark-glow spark-glow--embers" role="img" aria-label="Fading scatter of tiny embers"></div>
  </section>

  <p class="frame-label frame-label--last">LAST FRAME</p>
</div>
</body>
</html>
```